Our 2023 Comprehensive Needs Assessment needs a cover. We take data and produce an indepth beautiful report for our clients. Attached is the color palette we are going with. Let me know if you need me to send any additional information. This cover will be printed as well as used digitally.

```html
<!DOCTYPE html>
<html lang="en">
<head>
<meta charset="utf-8">
<title>2023 Comprehensive Needs Assessment – Cover</title>
<link rel="stylesheet" href="https://fonts.googleapis.com/css2?family=Bebas+Neue&display=swap">
<style>
  :root {
    --backdrop: #e2e2e2;
    --paper: #ffffff;
    --sky-yellow: #c9c94a;
    --sky-teal: #5f8f9a;
    --sky-blue: #2a5aa6;
    --field-yellow: #d9c21a;
    --field-green: #2f9a2a;
    --field-deep: #0f4a2e;
    --field-cyan: #1fc8e0;
    --band-green: #32880b;
    --stripe-green: #4aa507;
    --title-yellow: #f5d20a;
    --title-white: #ffffff;
  }
  html, body {
    margin: 0;
    width: 1200px;
    height: 1200px;
    overflow: hidden;
    background: var(--backdrop);
  }
  .cover {
    position: absolute;
    left: 226px;
    top: 40px;
    width: 747px;
    height: 1120px;
    background: var(--paper);
    overflow: hidden;
    font-family: "Bebas Neue", "Oswald", sans-serif;
  }
  .hero-photo {
    position: absolute;
    left: 0; top: 0;
    width: 747px; height: 386px;
    background: linear-gradient(100deg, var(--sky-yellow) 0%, var(--sky-teal) 45%, var(--sky-blue) 100%);
  }
  .year-mark {
    position: absolute;
    left: 0; top: 0;
    width: 747px; height: 420px;
  }
  .year-mark text {
    font-family: "Bebas Neue", "Oswald", sans-serif;
    fill: var(--paper);
  }
  .data-photo {
    position: absolute;
    left: 0; top: 422px;
    width: 747px; height: 466px;
    background:
      linear-gradient(90deg, var(--field-yellow) 0%, #8fbf22 22%, var(--field-green) 40%, var(--field-deep) 62%, #1b8a7a 82%, var(--field-green) 100%);
  }
  .data-photo::after {
    content: "";
    position: absolute;
    left: 300px; top: 230px;
    width: 420px; height: 150px;
    background: radial-gradient(ellipse at center, rgba(31,200,224,0.55) 0%, rgba(31,200,224,0) 70%);
  }
  .chevron {
    position: absolute;
    left: 0; top: 422px;
    width: 747px; height: 466px;
  }
  .title-band {
    position: absolute;
    left: 0; top: 924px;
    width: 747px; height: 196px;
    background: var(--band-green);
  }
  .title-band svg {
    position: absolute;
    left: 0; top: 0;
  }
  .title-block {
    position: absolute;
    left: 0; right: 0; top: 42px;
    text-align: center;
    letter-spacing: 0.5px;
  }
  .district-name {
    margin: 0;
    color: var(--title-yellow);
    font-size: 52px;
    line-height: 1;
    font-weight: 400;
    padding-left: 26px;
  }
  .report-title {
    margin: 8px 0 0;
    color: var(--title-white);
    font-size: 52px;
    line-height: 1;
    font-weight: 400;
    padding-left: 26px;
  }
</style>
</head>
<body>
  <main class="cover">
    <div class="hero-photo" role="img" aria-label="City skyline under a yellow-to-blue sky with rising arrows and people icons"></div>

    <svg class="year-mark" viewBox="0 0 747 420" aria-label="2023">
      <text x="162" y="396" font-size="410" textLength="585" lengthAdjust="spacingAndGlyphs">2023</text>
    </svg>

    <div class="data-photo" role="img" aria-label="Yellow-toned city street at left and glowing green and cyan data bar chart at right"></div>

    <svg class="chevron" viewBox="0 0 747 466" aria-hidden="true">
      <polygon points="60,0 162,0 102,103 313,466 209,466 0,102 0,0" fill="#ffffff"/>
      <rect x="0" y="0" width="60" height="0" fill="#ffffff"/>
    </svg>

    <section class="title-band">
      <svg width="747" height="196" viewBox="0 0 747 196" aria-hidden="true">
        <polygon points="560,196 680,0 747,0 747,20 640,196" fill="var(--stripe-green)"/>
        <polygon points="680,196 747,86 747,150 720,196" fill="var(--stripe-green)"/>
        <polygon points="470,196 590,0 620,0 500,196" fill="var(--stripe-green)" opacity="0.6"/>
      </svg>
      <div class="title-block">
        <h1 class="district-name">Maplecrest School District</h1>
        <h2 class="report-title">Comprehensive Needs Assessment</h2>
      </div>
    </section>
  </main>
</body>
</html>
```